Power Point Template for Company

I would like a power point template for my company. This will be the template that we use for all presentations. I have attached our company logo and would like it incorporated into the template. Thanks.

```html
<!DOCTYPE html>
<html lang="en">
<head>
<meta charset="utf-8">
<title>Vireo Studio – Presentation Template</title>
<link rel="stylesheet" href="https://fonts.googleapis.com/css2?family=Orbitron:wght@700;900&family=Roboto:wght@400;700&display=swap">
<style>
:root{
  --orange:#fb7a0c;
  --ink:#111111;
  --text:#222222;
  --white:#ffffff;
  --stage:#6e6e6e;
  --ring:#e4e4e4;
  --dark:#1d1b1a;
}
*{margin:0;padding:0;box-sizing:border-box}
html,body{width:1200px;height:4121px;overflow:hidden}
body{background:var(--stage);position:relative;font-family:"Roboto",Arial,sans-serif;color:var(--text)}
.slide{position:absolute;left:24px;width:1152px;height:646px;background:var(--white);overflow:hidden}
.side-bar{position:absolute;left:0;top:0;width:35px;height:100%;background:var(--orange)}
.badge{position:absolute;left:8px;top:25px;width:90px;height:90px;border-radius:50%;background:var(--white);border:4px solid var(--orange);display:flex;align-items:center;justify-content:center}
.badge span{width:62px;height:62px;border-radius:50%;background:var(--orange)}
.slide-title{position:absolute;left:112px;top:40px;font-family:"Orbitron",sans-serif;font-weight:900;font-size:31px;letter-spacing:1px;color:var(--ink);text-transform:uppercase}
.title-rule{position:absolute;left:112px;top:94px;width:67px;height:4px;background:var(--orange)}
.body-copy{position:absolute;font-size:13.5px;line-height:29px;color:var(--text)}
.diamond{position:absolute;width:26px;height:26px;background:var(--orange);transform:rotate(45deg)}

/* cover */
.brand{position:absolute;left:59px;top:150px;display:flex;align-items:center;gap:14px}
.brand-dot{width:60px;height:60px;border-radius:50%;background:var(--orange)}
.brand-name{font-family:"Orbitron",sans-serif;font-weight:700;font-size:26px;color:var(--ink);letter-spacing:2px}
.cover-title{position:absolute;left:59px;top:240px;font-family:"Orbitron",sans-serif;font-weight:900;font-size:50px;line-height:86px;color:var(--ink);letter-spacing:1px}
.cover-title em{font-style:normal;color:var(--orange)}
.cover-lead{position:absolute;left:59px;top:418px;width:540px;font-size:20px;line-height:41px;color:var(--text)}
.cover-disc{position:absolute;left:636px;top:96px;width:460px;height:460px;border-radius:50%;background:var(--orange);display:flex;align-items:center;justify-content:center;font-family:"Orbitron",sans-serif;font-weight:700;font-size:34px;color:var(--white);letter-spacing:2px}

/* mission */
.point{position:absolute;left:650px;width:445px}
.point-head{height:61px;background:var(--orange);color:var(--white);font-weight:700;font-size:19px;display:flex;align-items:center;justify-content:center}
.point-note{margin-top:16px;text-align:center;font-size:11.5px;line-height:22px;color:var(--text)}

/* faculty */
.faculty-accent{position:absolute;left:1051px;top:246px;width:101px;height:141px;background:var(--orange)}
.faculty-photo{position:absolute;left:499px;top:46px;width:595px;height:326px;background:linear-gradient(135deg,#6a4a30,#a97d55 50%,#5b3e28)}

/* broad */
.member-photo{position:absolute;width:118px;height:118px;border-radius:50%;background:linear-gradient(160deg,#c8ccd2,#5f6672)}
.member-text{position:absolute;width:300px;font-size:14px;line-height:28px;color:var(--text)}

/* services */
.services-art{position:absolute;left:0;top:0}
.hub-name{position:absolute;left:481px;top:352px;width:200px;text-align:center;font-family:"Orbitron",sans-serif;font-weight:700;font-size:24px;color:var(--ink);letter-spacing:2px}
.service-text{position:absolute;width:240px;font-size:14px;line-height:32px;color:var(--text)}

/* contact */
.contact{background:linear-gradient(135deg,#2a2623,#141210 55%,#2b221b)}
.contact-photo{position:absolute;inset:0;background:linear-gradient(180deg,rgba(60,52,46,.55),rgba(20,18,16,.2))}
.contact-title{position:absolute;left:59px;top:130px;font-family:"Orbitron",sans-serif;font-weight:900;font-size:34px;color:var(--white);letter-spacing:1px}
.contact-rule{position:absolute;left:59px;top:192px;width:93px;height:4px;background:var(--white)}
.contact-row{position:absolute;left:61px;display:flex;align-items:center;gap:22px;color:var(--white);font-size:22px}
.contact-icon{width:58px;height:58px;border-radius:50%;background:var(--white);display:flex;align-items:center;justify-content:center}
.contact-brand{position:absolute;left:744px;top:140px;display:flex;align-items:center;gap:16px}
.contact-brand .brand-dot{width:96px;height:96px;background:var(--white)}
.contact-brand .brand-name{color:var(--white);font-size:32px}
</style>
</head>
<body>

<!-- Cover -->
<section class="slide" style="top:29px">
  <div class="brand"><span class="brand-dot"></span><span class="brand-name">VIREO STUDIO</span></div>
  <h1 class="cover-title">WELCOME TO<br>VIREO <em>STUDIO</em></h1>
  <p class="cover-lead">Lorem ipsum dolor sit amet, consectetur adipiscing elit, sed do eiusmod dolore magna aliqua.</p>
  <div class="cover-disc">VIREO</div>
</section>

<!-- Mission -->
<section class="slide" style="top:710px">
  <div class="side-bar"></div>
  <div class="badge"><span></span></div>
  <h2 class="slide-title">Our Mission</h2>
  <div class="title-rule"></div>
  <div class="body-copy" style="left:112px;top:118px;width:470px">
    <p>Lorem ipsum dolor sit amet, consectetur adipiscing elit, sed do eiusmod tempor incididunt ut labore et dolore magna aliqua. Ut enim ad minim veniam, quis nostrud exercitation ullamco laboris nisi ut aliquip ex ea commodo consequat. Duis aute irure dolor in reprehenderit in voluptate velit esse cillum dolore eu fugiat nulla pariatur.</p>
    <p style="margin-top:28px">Excepteur sint occaecat cupidatat non proident, sunt in culpa qui officia deserunt mollit anim id est laborum.Sed ut perspiciatis unde omnis iste natus error sit voluptatem accusantium doloremque laudantium, totam rem aperiam, eaque ipsa quae ab illo inventore veritatis et quasi architecto beatae vitae dicta sunt explicabo.</p>
    <p style="margin-top:28px">Nemo enim ipsam voluptatem quia voluptas sit aspernatur aut odit aut fugit, sed quia consequuntur magni dolores eos qui ratione voluptatem sequi nesciunt.</p>
  </div>
  <div class="point" style="top:130px"><div class="point-head">Lorem ipsum dolor sit amet</div><p class="point-note">Duis aute irure dolor in reprehenderit in voluptate velit esse cillum<br>dolore eu fugiat nulla pariatur.</p></div>
  <div class="point" style="top:274px"><div class="point-head">Lorem ipsum dolor sit amet</div><p class="point-note">Duis aute irure dolor in reprehenderit in voluptate velit esse cillum<br>dolore eu fugiat nulla pariatur.</p></div>
  <div class="point" style="top:424px"><div class="point-head">Lorem ipsum dolor sit amet</div><p class="point-note">Duis aute irure dolor in reprehenderit in voluptate velit esse cillum<br>dolore eu fugiat nulla pariatur.</p></div>
</section>

<!-- Faculty -->
<section class="slide" style="top:1392px">
  <div class="side-bar"></div>
  <div class="badge"><span></span></div>
  <h2 class="slide-title">Our Faculty</h2>
  <div class="title-rule"></div>
  <div class="body-copy" style="left:112px;top:118px;width:345px">
    <p><b>Lorem ipsum dolor sit amet</b>, consectetur adipiscing elit, sed do eiusmod tempor incididunt ut labore et dolore magna aliqua. Ut enim ad minim veniam, quis nostrud exercitation ullamco laboris nisi ut aliquip ex ea commodo consequat. Duis aute irure dolor in reprehenderit in voluptate velit esse cillum dolore eu fugiat nulla pariatur.</p>
    <p style="margin-top:58px">Excepteur sint occaecat cupidatat non proident, sunt in culpa qui officia deserunt mollit anim id est laborum.Sed ut perspiciatis unde omnis iste natus error sit voluptatem accusantium doloremque laudantium, totam rem aperiam, eaque ipsa quae ab illo inventore veritatis et quasi architecto beatae vitae dicta sunt explicabo.</p>
  </div>
  <div class="faculty-accent"></div>
  <div class="faculty-photo" role="img" aria-label="Team around a wooden table with laptops, overlaid with a digital marketing word cloud"></div>
  <p class="body-copy" style="left:509px;top:410px;width:560px">Nemo enim ipsam voluptatem quia voluptas sit aspernatur aut odit aut fugit, sed quia consequuntur magni dolores eos qui ratione voluptatem sequi nesciunt. Neque porro quisquam est, qui dolorem ipsum quia dolor sit amet, consectetur, adipisci velit, sed quia non numquam eius modi tempora incidunt ut labore et dolore magnam aliquam quaerat voluptatem. Ut enim ad minima veniam, quis nostrum exercitationem ullam corporis suscipit laboriosam, nisi ut aliquid ex ea commodi consequatur?</p>
  <div class="diamond" style="left:1107px;top:558px"></div>
</section>

<!-- Board -->
<section class="slide" style="top:2074px">
  <div class="side-bar"></div>
  <div class="badge"><span></span></div>
  <h2 class="slide-title">Meet Our Broad</h2>
  <div class="title-rule"></div>

  <div class="member-photo" style="left:101px;top:141px" role="img" aria-label="Portrait of a board member"></div>
  <p class="member-text" style="left:237px;top:140px"><b>Lorem ipsum dolor</b> sit amet, consectetur adipiscing elit, sed do eiusmod tempor incididunt ut labore et commodo consequat.</p>
  <div class="member-photo" style="left:648px;top:141px" role="img" aria-label="Portrait of a board member"></div>
  <p class="member-text" style="left:784px;top:140px"><b>Lorem ipsum dolor</b> sit amet, consectetur adipiscing elit, sed do eiusmod tempor incididunt ut labore et commodo consequat.</p>

  <div class="member-photo" style="left:101px;top:311px" role="img" aria-label="Portrait of a board member"></div>
  <p class="member-text" style="left:237px;top:309px"><b>Lorem ipsum dolor</b> sit amet, consectetur adipiscing elit, sed do eiusmod tempor incididunt ut labore et commodo consequat.</p>
  <div class="member-photo" style="left:648px;top:311px" role="img" aria-label="Portrait of a board member"></div>
  <p class="member-text" style="left:784px;top:309px"><b>Lorem ipsum dolor</b> sit amet, consectetur adipiscing elit, sed do eiusmod tempor incididunt ut labore et commodo consequat.</p>

  <div class="member-photo" style="left:101px;top:479px" role="img" aria-label="Portrait of a board member"></div>
  <p class="member-text" style="left:237px;top:478px"><b>Lorem ipsum dolor</b> sit amet, consectetur adipiscing elit, sed do eiusmod tempor incididunt ut labore et commodo consequat.</p>
  <div class="member-photo" style="left:648px;top:479px" role="img" aria-label="Portrait of a board member"></div>
  <p class="member-text" style="left:784px;top:478px"><b>Lorem ipsum dolor</b> sit amet, consectetur adipiscing elit, sed do eiusmod tempor incididunt ut labore et commodo consequat.</p>

  <div class="diamond" style="left:1104px;top:581px"></div>
</section>

<!-- Services -->
<section class="slide" style="top:2755px">
  <div class="side-bar"></div>
  <div class="badge"><span></span></div>
  <h2 class="slide-title">Our Services</h2>
  <div class="title-rule"></div>

  <svg class="services-art" width="1152" height="646" viewBox="0 0 1152 646">
    <circle cx="581" cy="370" r="216" fill="none" stroke="#333" stroke-width="1.5" stroke-dasharray="5 5"/>
    <circle cx="581" cy="370" r="186" fill="none" stroke="var(--ring)" stroke-width="20"/>
    <g stroke="#fff" stroke-width="2.5" fill="none" stroke-linecap="round" stroke-linejoin="round">
      <circle cx="429" cy="200" r="45" fill="var(--orange)" stroke="none"/>
      <rect x="413" y="184" width="32" height="32" rx="3"/><path d="M419 208l7-8 6 6 7-9"/>
      <circle cx="739" cy="200" r="45" fill="var(--ink)" stroke="none"/>
      <path d="M723 196l20-10v28l-20-10z"/><path d="M723 196v8"/><path d="M750 194l6-4M750 200h7M750 206l6 4"/>
      <circle cx="368" cy="355" r="45" fill="var(--ink)" stroke="none"/>
      <rect x="350" y="340" width="36" height="26" rx="3"/><path d="M350 348h36"/><path d="M372 360l10 12 2-6 6-2z" fill="#fff"/>
      <circle cx="800" cy="355" r="45" fill="var(--orange)" stroke="none"/>
      <circle cx="788" cy="343" r="6"/><circle cx="812" cy="343" r="6"/><circle cx="788" cy="367" r="6"/><circle cx="812" cy="367" r="6"/><path d="M794 343h12M794 367h12"/>
      <circle cx="432" cy="514" r="45" fill="var(--orange)" stroke="none"/>
      <rect x="416" y="500" width="22" height="18" rx="2"/><rect x="428" y="512" width="22" height="18" rx="2"/>
      <circle cx="736" cy="514" r="45" fill="var(--ink)" stroke="none"/>
      <rect x="718" y="504" width="26" height="20" rx="3"/><path d="M744 510l12-7v22l-12-7"/>
    </g>
    <text x="731" y="519" font-family="Roboto, sans-serif" font-size="10" font-weight="700" fill="#fff" text-anchor="middle">AD</text>
  </svg>
  <div class="hub-name">VIREO</div>

  <p class="service-text" style="left:149px;top:168px">Lorem ipsum dolor sit amet,<br>incididunt dolore magna aliqua.</p>
  <p class="service-text" style="left:797px;top:168px">Lorem ipsum dolor sit amet,<br>incididunt dolore magna aliqua.</p>
  <p class="service-text" style="left:90px;top:323px">Lorem ipsum dolor sit amet,<br>incididunt dolore magna aliqua.</p>
  <p class="service-text" style="left:858px;top:323px">Lorem ipsum dolor sit amet,<br>incididunt dolore magna aliqua.</p>
  <p class="service-text" style="left:152px;top:482px">Lorem ipsum dolor sit amet,<br>incididunt dolore magna aliqua.</p>
  <p class="service-text" style="left:794px;top:482px">Lorem ipsum dolor sit amet,<br>incididunt dolore magna aliqua.</p>
</section>

<!-- Contact -->
<section class="slide contact" style="top:3437px">
  <div class="contact-photo" role="img" aria-label="Dimmed photo of a team working together in a busy office"></div>
  <h2 class="contact-title">GET IN TOUCH</h2>
  <div class="contact-rule"></div>
  <div class="contact-row" style="top:270px">
    <span class="contact-icon"><svg width="24" height="24" viewBox="0 0 24 24"><path d="M6.6 10.8a15 15 0 0 0 6.6 6.6l2.2-2.2a1 1 0 0 1 1-.25 11.4 11.4 0 0 0 3.6.57 1 1 0 0 1 1 1V20a1 1 0 0 1-1 1A17 17 0 0 1 3 4a1 1 0 0 1 1-1h3.5a1 1 0 0 1 1 1c0 1.25.2 2.45.57 3.57a1 1 0 0 1-.25 1z" fill="var(--orange)"/></svg></span>
    <span>+1 555 014 2277</span>
  </div>
  <div class="contact-row" style="top:366px">
    <span class="contact-icon"><svg width="24" height="24" viewBox="0 0 24 24"><rect x="2" y="5" width="20" height="14" rx="2" fill="var(--orange)"/><path d="M3 6l9 7 9-7" stroke="#fff" stroke-width="1.8" fill="none"/></svg></span>
    <span>hello@vireostudio.com</span>
  </div>
  <div class="contact-row" style="top:467px">
    <span class="contact-icon"><svg width="24" height="24" viewBox="0 0 24 24"><path d="M12 2a7 7 0 0 0-7 7c0 5.2 7 13 7 13s7-7.8 7-13a7 7 0 0 0-7-7z" fill="var(--orange)"/><circle cx="12" cy="9" r="2.6" fill="#fff"/></svg></span>
    <span>Lorem ipsum dolor sit amet.</span>
  </div>
  <div class="contact-brand"><span class="brand-dot"></span><span class="brand-name">VIREO STUDIO</span></div>
</section>

</body>
</html>
```